refurbishment of diamond cut alloy wheels

we need to design a flyer that will catch the eye of the customer to refurbish diamond cut alloy wheels. we refurbish the wheels by using the latest CNC machine to precision cut and resurface the wheel. we would like before and after pictures of maybe Kelvaron, DXT, Orsa wheels to give it a prestige look. The final design should communicate an expensive look and providing a good image for the business. The colours that I would like to use is black and red which should make the flyer stand out. The logo must sit on a black background without the wordings of specialists in HJ, Orsa etc and also without servicing, diagnostics etc as well. This flyer is just to communicate refurbishment of alloy wheels to high standard.

Target Market(s)

any members of the public and car dealerships

Industry/Entity Type

Automotive

Colors

Designer to choose colors to be used in the design.

Requirements
Must have
• Wow factor with great images of wheels
Nice to have
• Maybe on the front of the flyer it has a picture of a wheel and then on the back of the flyer it has before and after pictures to show how just how incredible it is to refurbish wheels
Should not have
• other makes of wheels apart from DXT, Orsa, and any other high end makes of vehicles wheels

```html
<!DOCTYPE html>
<html lang="en">
<head>
<meta charset="utf-8">
<title>Corvane Motors – Alloy Wheel Refurbishment Flyer</title>
<link rel="stylesheet" href="https://fonts.googleapis.com/css2?family=Archivo+Black&family=Montserrat:wght@400;500;600;700&display=swap">
<style>
  :root {
    --backdrop: #93abc1;
    --backdrop-edge: #6f8aa3;
    --page-black: #0b0b0c;
    --page-grey: #1b1c1f;
    --red: #c8161d;
    --red-dark: #7d0a0f;
    --red-light: #e2343a;
    --white: #ffffff;
    --soft-white: #e9e9ea;
    --muted: #c9c9cc;
    --silver: #d9dadc;
    --photo-dark: #17181b;
    --photo-mid: #3a3c41;
    --photo-light: #8a8d93;
    --photo-yellow: #d9a514;
  }
  * { box-sizing: border-box; margin: 0; padding: 0; }
  html, body { width: 1200px; height: 3158px; overflow: hidden; }
  body {
    background: var(--backdrop);
    box-shadow: inset 0 0 0 6px var(--backdrop-edge);
    font-family: "Montserrat", Arial, sans-serif;
    color: var(--white);
    position: relative;
  }
  .page {
    position: absolute;
    left: 54px;
    width: 1090px;
    background: radial-gradient(ellipse at 50% 60%, var(--page-grey) 0%, var(--page-black) 70%);
    box-shadow: 0 6px 22px rgba(0,0,0,0.45);
    overflow: hidden;
  }
  .page--front { top: 41px; height: 1513px; }
  .page--back { top: 1595px; height: 1522px; }

  /* ---------- Front ---------- */
  .front-top-strip {
    position: absolute; left: 0; top: 0; width: 100%; height: 90px;
    background: linear-gradient(180deg, #1e1f22, #0b0b0c);
  }
  .wheel-photo {
    position: absolute;
  }
  .wheel-photo--hero-left {
    left: 0; top: 150px; width: 640px; height: 920px;
    background:
      radial-gradient(circle at 55% 62%, var(--photo-mid) 0%, var(--photo-dark) 38%, #0d0d0f 55%, transparent 56%),
      linear-gradient(160deg, var(--photo-dark) 0%, #202125 50%, var(--photo-yellow) 51%, #8c6a0c 75%, #111 100%);
    clip-path: polygon(0 0, 100% 0, 100% 100%, 0 100%);
  }
  .wheel-photo--hero-right {
    left: 560px; top: 0; width: 530px; height: 800px;
    background:
      radial-gradient(circle at 62% 48%, var(--photo-light) 0%, var(--photo-mid) 20%, var(--photo-dark) 48%, #0c0c0e 70%);
    clip-path: polygon(90px 0, 100% 0, 100% 100%, 0 100%, 0 60px);
    border-left: 4px solid var(--silver);
  }
  .brand {
    position: absolute; display: flex; align-items: center; gap: 16px;
  }
  .brand__mark {
    width: 56px; height: 56px; background: var(--red);
  }
  .brand__name {
    font-family: "Archivo Black", Arial, sans-serif;
    color: var(--white); line-height: 1; text-transform: uppercase;
  }
  .brand--front { left: 70px; top: 175px; padding: 22px 30px; background: var(--page-black); }
  .brand--front .brand__name { font-size: 46px; }

  .title-banner {
    position: absolute; left: 390px; top: 795px; width: 700px; height: 315px;
    background: linear-gradient(180deg, var(--red-light) 0%, var(--red) 45%, var(--red-dark) 100%);
    clip-path: polygon(60px 0, 100% 0, 100% 100%, 0 100%);
    padding: 40px 30px 0 100px;
  }
  .title-banner__text {
    font-family: "Archivo Black", Arial, sans-serif;
    font-size: 56px; line-height: 1.22; text-transform: uppercase; color: var(--white);
    text-shadow: 0 3px 4px rgba(0,0,0,0.45);
  }
  .title-banner__text .accent { color: var(--soft-white); opacity: 0.85; }
  .silver-rule {
    position: absolute; left: 0; top: 1110px; width: 100%; height: 10px;
    background: linear-gradient(90deg, #2a2b2e 0%, var(--silver) 45%, #ffffff 60%, #55575b 100%);
  }
  .front-intro {
    position: absolute; left: 90px; top: 1175px; width: 910px;
    text-align: center; font-size: 35px; line-height: 1.3; font-weight: 500; color: var(--soft-white);
  }
  .divider {
    position: absolute; height: 3px; background: linear-gradient(90deg, rgba(255,255,255,0.1), rgba(255,255,255,0.85), rgba(255,255,255,0.1));
  }
  .divider--front { left: 70px; width: 950px; top: 1340px; }
  .front-contact-note {
    position: absolute; left: 70px; top: 1385px; width: 480px;
    font-size: 25px; line-height: 1.3; color: var(--muted);
  }
  .phone-button {
    position: absolute; display: flex; align-items: center; gap: 18px; justify-content: center;
    background: linear-gradient(180deg, var(--red-light) 0%, var(--red) 50%, var(--red-dark) 100%);
    border: 3px solid var(--silver); border-radius: 16px;
    transform: skewX(-8deg);
    box-shadow: 0 4px 10px rgba(0,0,0,0.6);
  }
  .phone-button > * { transform: skewX(8deg); }
  .phone-button__number { font-size: 40px; font-weight: 600; color: var(--white); letter-spacing: 1px; }
  .phone-button svg { width: 36px; height: 36px; }
  .phone-button--front { left: 615px; top: 1380px; width: 395px; height: 82px; }

  /* ---------- Back ---------- */
  .back-title-tab {
    position: absolute; left: 0; top: 54px; width: 690px; height: 120px;
    background: linear-gradient(180deg, var(--red-light), var(--red) 50%, var(--red-dark));
    clip-path: polygon(0 0, 100% 0, 92% 100%, 0 100%);
    padding: 14px 0 0 70px;
    font-size: 34px; font-weight: 700; line-height: 1.3; color: var(--white);
  }
  .brand--back { left: 740px; top: 90px; }
  .brand--back .brand__mark { width: 44px; height: 44px; }
  .brand--back .brand__name { font-size: 34px; }

  .comparison-photo {
    position: absolute; top: 210px; width: 458px; height: 405px;
    border: 5px solid var(--silver); border-radius: 30px;
    transform: skewX(-5deg);
    box-shadow: 0 6px 14px rgba(0,0,0,0.7);
  }
  .comparison-photo--before {
    left: 104px;
    background: radial-gradient(circle at 50% 55%, #e3e3e3 0%, #6a6c70 22%, #cfcfd1 40%, #3b3c40 62%, #6e6a63 100%);
  }
  .comparison-photo--after {
    left: 552px;
    background: radial-gradient(circle at 50% 55%, #f1f1f1 0%, #5c5e62 22%, #e6e6e8 40%, #2e2f33 62%, #5d6066 100%);
  }
  .comparison-label {
    position: absolute; top: 640px; height: 65px; width: 340px;
    background: linear-gradient(180deg, var(--red-light), var(--red) 50%, var(--red-dark));
    border: 3px solid var(--silver); border-radius: 12px;
    transform: skewX(-8deg);
    display: flex; align-items: center; justify-content: center;
  }
  .comparison-label span { transform: skewX(8deg); font-size: 38px; font-weight: 600; }
  .comparison-label--before { left: 185px; }
  .comparison-label--after { left: 640px; }
  .divider--back-top { left: 70px; width: 950px; top: 745px; height: 2px; }

  .coverage-text {
    position: absolute; left: 110px; top: 790px; width: 870px;
    text-align: center; font-size: 29px; line-height: 1.35; color: var(--soft-white);
  }
  .detail-text {
    position: absolute; left: 120px; width: 850px;
    text-align: center; font-size: 18px; line-height: 1.45; color: var(--muted);
  }
  .detail-text--one { top: 975px; }
  .detail-text--two { top: 1055px; }
  .divider--back-bottom { left: 70px; width: 950px; top: 1290px; }
  .closing-call {
    position: absolute; left: 70px; top: 1340px; text-transform: uppercase; color: var(--white);
  }
  .closing-call__lead { font-size: 25px; letter-spacing: 1px; }
  .closing-call__main { font-size: 42px; letter-spacing: 1px; margin-top: 6px; }
  .phone-button--back { left: 610px; top: 1345px; width: 398px; height: 90px; }
</style>
</head>
<body>

<section class="page page--front">
  <div class="front-top-strip"></div>
  <div class="wheel-photo wheel-photo--hero-left" role="img" aria-label="Photo of a black diamond cut alloy wheel on a yellow sports car"></div>
  <div class="wheel-photo wheel-photo--hero-right" role="img" aria-label="Close-up photo of a dark multi-spoke alloy wheel"></div>

  <div class="brand brand--front">
    <span class="brand__mark"></span>
    <span class="brand__name">Corvane Motors</span>
  </div>

  <div class="title-banner">
    <h1 class="title-banner__text">Alloy <span class="accent">Wheel</span><br>Refurbishment<br>Specialists</h1>
  </div>
  <div class="silver-rule"></div>

  <p class="front-intro">We refurbish the wheels by using the latest CNC machine to precision cut and resurface the wheel.</p>

  <div class="divider divider--front"></div>
  <p class="front-contact-note">If you need premier Alloy Wheel Refurbishment services in Slough, please contact us:</p>
  <div class="phone-button phone-button--front">
    <svg viewBox="0 0 24 24" aria-hidden="true"><path fill="#fff" d="M6.6 10.8a15.2 15.2 0 0 0 6.6 6.6l2.2-2.2c.3-.3.7-.4 1-.2 1.1.4 2.3.6 3.6.6.6 0 1 .4 1 1V20c0 .6-.4 1-1 1C10.6 21 3 13.4 3 4c0-.6.4-1 1-1h3.5c.6 0 1 .4 1 1 0 1.3.2 2.5.6 3.6.1.3 0 .7-.2 1l-2.3 2.2z"/></svg>
    <span class="phone-button__number">01632 960 418</span>
  </div>
</section>

<section class="page page--back">
  <h2 class="back-title-tab">Alloy wheel Refurbishment<br>Specialists in and around Slough</h2>
  <div class="brand brand--back">
    <span class="brand__mark"></span>
    <span class="brand__name">Corvane Motors</span>
  </div>

  <div class="comparison-photo comparison-photo--before" role="img" aria-label="Before photo: worn and corroded silver multi-spoke alloy wheel"></div>
  <div class="comparison-photo comparison-photo--after" role="img" aria-label="After photo: the same alloy wheel refurbished with a bright diamond cut finish"></div>
  <div class="comparison-label comparison-label--before"><span>Before</span></div>
  <div class="comparison-label comparison-label--after"><span>After</span></div>
  <div class="divider divider--back-top"></div>

  <p class="coverage-text">We cater to all locations in and around Colnbrook, Windsor, Hayes, Hounslow, Staines, Ascot and Ashford. For all car body modifications and restorations get in touch with our team of experts today!</p>
  <p class="detail-text detail-text--one">If you are looking to refresh the look of your car but don't want the expense of new alloys, with a wide range of limited edition colours to choose from why not consider customising and refurbishing your existing alloys?</p>
  <p class="detail-text detail-text--two">If you've had your alloy wheels long enough for them to require alloy refurbishment you can choose from a wide range of colours for refurbishment or choose a brand new set from our comprehensive range. At Corvane Wheels &amp; Tyres, we stock an extensive range of the latest designs from all the leading suppliers and manufacturers so you are sure to find a stylish new design.</p>

  <div class="divider divider--back-bottom"></div>
  <div class="closing-call">
    <p class="closing-call__lead">If your alloys need refurbishment</p>
    <p class="closing-call__main">Contact us today</p>
  </div>
  <div class="phone-button phone-button--back">
    <svg viewBox="0 0 24 24" aria-hidden="true"><path fill="#fff" d="M6.6 10.8a15.2 15.2 0 0 0 6.6 6.6l2.2-2.2c.3-.3.7-.4 1-.2 1.1.4 2.3.6 3.6.6.6 0 1 .4 1 1V20c0 .6-.4 1-1 1C10.6 21 3 13.4 3 4c0-.6.4-1 1-1h3.5c.6 0 1 .4 1 1 0 1.3.2 2.5.6 3.6.1.3 0 .7-.2 1l-2.3 2.2z"/></svg>
    <span class="phone-button__number">01632 960 418</span>
  </div>
</section>

</body>
</html>
```